Déménagement Résidentiel & Commerciale

Déménagement Vellour

Depuis des années, Déménagement Vellour déplace ses clients dans et autour de la grande région de Montréal. Avec une équipe de déménageurs expérimentés, et un accent sur le service à la clientèle. Déménagement Vellour cherche à offrir une expérience de première classe à tous ses clients.

Target Market(s)

people selling or buying homes
people going to the bank for a load or real estate

company discounts

Requirements
Must have
• inviting
suprise e
Nice to have
• packages
why vellour

we offer storage solution bundles for products online reservation many methodes of payment

must also be french first then english and chinees mandarin
Should not have
• dates on promotion
prices

```html
<!DOCTYPE html>
<html lang="fr">
<head>
<meta charset="utf-8">
<title>Déménagement Vellour – Dépliant</title>
<link href="https://fonts.googleapis.com/css2?family=Source+Sans+3:ital,wght@0,400;0,600;0,700;1,400&family=Russo+One&display=swap" rel="stylesheet">
<style>
  :root{
    --navy:#2c426d;
    --navy-deep:#23375c;
    --navy-soft:#3a5282;
    --white:#ffffff;
    --ink:#2a3550;
    --grey-text:#4b4f58;
    --icon-grey:#d4d3cc;
    --pill:#e6e4dc;
    --star:#f2b51d;
    --backdrop:#ecebe8;
  }
  *{margin:0;padding:0;box-sizing:border-box}
  html,body{width:1200px;height:873px;overflow:hidden}
  body{background:var(--backdrop);font-family:"Source Sans 3",sans-serif;position:relative}
  .flyer{position:absolute;left:302px;top:15px;width:596px;height:842px;background:var(--white);overflow:hidden;box-shadow:0 2px 10px rgba(0,0,0,.15)}
  .flyer > *{position:absolute}
  .bg-shapes{left:0;top:0;width:596px;height:842px}
  .brand{left:355px;top:14px;text-align:right;width:220px}
  .brand-name{font-family:"Russo One",sans-serif;font-size:34px;color:var(--navy);letter-spacing:1px;line-height:1}
  .brand-tag{font-family:"Russo One",sans-serif;font-size:10px;color:var(--navy);margin-top:6px}
  .hero-copy{left:20px;top:58px;width:245px;text-align:center;color:var(--white)}
  .hero-title{font-size:22.5px;font-weight:600;line-height:27px;text-transform:uppercase}
  .hero-lead{font-size:13px;line-height:16px;margin-top:6px}
  .cta{display:inline-block;margin-top:13px;background:var(--pill);color:var(--navy);font-weight:700;font-size:14.5px;padding:4px 16px;border-radius:14px;text-transform:uppercase}
  .hero-phone{margin-top:10px;font-size:16.5px;font-weight:700;display:flex;align-items:center;justify-content:center;gap:7px}
  .services{left:0;top:326px;width:596px;display:flex;justify-content:space-between;padding:0 46px 0 60px}
  .service{width:150px;text-align:center}
  .service svg{display:block;margin:0 auto 14px;height:54px}
  .service h3{font-size:12px;font-weight:700;color:var(--navy);line-height:14px;text-transform:uppercase}
  .service p{font-size:8.5px;color:var(--grey-text);line-height:11px;margin-top:3px;padding:0 8px}
  .about{left:40px;top:551px;width:516px;text-align:center;color:var(--white)}
  .about h2{font-size:14px;font-weight:700;text-transform:uppercase;color:#e4e6ec}
  .about p{font-size:11.5px;line-height:15px;margin-top:10px}
  .review{top:632px;width:242px;color:var(--white)}
  .review.one{left:40px}
  .review.two{left:319px}
  .stars{color:var(--star);font-size:17px;letter-spacing:1px;line-height:16px}
  .review p{font-size:8.3px;font-style:italic;line-height:10px;margin-top:4px;text-align:justify}
  .fleet{left:305px;top:698px;display:flex;gap:8px}
  .fleet span{display:block;width:83px;height:83px;border-radius:50%;border:2px solid var(--white);background:radial-gradient(circle at 50% 45%,#d9dde3,#8d96a4 60%,#3d4450)}
  .crew{left:18px;top:684px;width:292px;height:158px;background:linear-gradient(180deg,rgba(60,84,132,0) 0%,#3a5890 45%,#1f3566 100%)}
  .contact{left:296px;top:795px;width:300px;height:47px;background:var(--white);text-align:right;padding:2px 24px 0 0;color:var(--navy);font-weight:700}
  .contact-phone{font-size:16.5px;line-height:20px;display:flex;justify-content:flex-end;align-items:center;gap:6px}
  .contact-web{font-size:14.5px;line-height:18px}
</style>
</head>
<body>
<main class="flyer">
  <svg class="bg-shapes" viewBox="0 0 596 842">
    <defs>
      <linearGradient id="movePhoto" x1="0" y1="0" x2="1" y2="1">
        <stop offset="0" stop-color="#e8e9ec"/>
        <stop offset=".5" stop-color="#b9bcc3"/>
        <stop offset="1" stop-color="#8c8478"/>
      </linearGradient>
      <linearGradient id="bluePhoto" x1="0" y1="0" x2="0" y2="1">
        <stop offset="0" stop-color="#34507f"/>
        <stop offset="1" stop-color="#2b416b"/>
      </linearGradient>
    </defs>
    <rect class="hero-photo" x="0" y="0" width="596" height="330" fill="url(#movePhoto)" role="img" aria-label="Photo de déménageurs chargeant des boîtes dans un camion devant un couple"/>
    <rect class="hero-panel" x="20" y="0" width="245" height="330" fill="var(--navy)" opacity=".94"/>
    <polygon class="white-break" points="0,296 265,322 596,290 596,842 0,842" fill="var(--white)"/>
    <polygon class="about-band" points="0,509 298,476 596,509 596,842 0,842" fill="url(#bluePhoto)" role="img" aria-label="Photo estompée d'une équipe de déménagement en fond"/>
  </svg>

  <div class="brand">
    <div class="brand-name">VELLOUR</div>
    <div class="brand-tag">Déménagement &amp; Transport</div>
  </div>

  <section class="hero-copy">
    <h1 class="hero-title">Commencez votre prochain déménagement ici</h1>
    <p class="hero-lead">Le déménagement peut être stressant.<br>Nous pouvons aider.</p>
    <span class="cta">Réserver maintenant</span>
    <div class="hero-phone">
      <svg width="12" height="15" viewBox="0 0 12 15"><rect x="1" y="1" width="10" height="13" rx="2" fill="none" stroke="currentColor" stroke-width="2"/><rect x="4" y="4" width="4" height="6" fill="currentColor"/></svg>
      438.555.0147
    </div>
  </section>

  <section class="services">
    <article class="service">
      <svg viewBox="0 0 74 54" width="74"><polygon points="37,2 4,22 70,22" fill="var(--icon-grey)"/><rect x="8" y="22" width="58" height="30" fill="var(--icon-grey)"/><rect x="16" y="32" width="10" height="10" fill="#fff"/><rect x="32" y="32" width="10" height="20" fill="#fff"/><rect x="48" y="32" width="10" height="10" fill="#fff"/></svg>
      <h3>Déménagement<br>résidentiel</h3>
      <p>Déménager dans votre nouvelle maison ne pourrait pas être plus facile. Notre équipe est prête à vous aider.</p>
    </article>
    <article class="service">
      <svg viewBox="0 0 56 54" width="56"><rect x="4" y="18" width="22" height="36" fill="var(--icon-grey)"/><rect x="24" y="2" width="28" height="52" fill="var(--icon-grey)"/><g stroke="#fff" stroke-width="2"><line x1="8" y1="26" x2="22" y2="26"/><line x1="8" y1="34" x2="22" y2="34"/><line x1="8" y1="42" x2="22" y2="42"/><line x1="38" y1="8" x2="38" y2="54"/></g></svg>
      <h3>Transport<br>commercial</h3>
      <p>A votre service pour tous vos transport commerciaux. Service rapide, efficace et digne de confiance!</p>
    </article>
    <article class="service">
      <svg viewBox="0 0 80 54" width="80"><rect x="28" y="4" width="24" height="20" fill="var(--icon-grey)"/><rect x="4" y="28" width="24" height="22" fill="var(--icon-grey)"/><rect x="30" y="26" width="22" height="22" fill="var(--icon-grey)"/><rect x="54" y="28" width="24" height="22" fill="var(--icon-grey)"/></svg>
      <h3>Fournitures<br>de déménagement</h3>
      <p>Toutes les fournitures dont vous aurez besoin pour compléter votre déménagement.</p>
    </article>
  </section>

  <section class="about">
    <h2>Déménagement Vellour</h2>
    <p>Depuis des années, Déménagement Vellour déplace ses clients dans et autour de la grande région de Montréal. Avec une équipe de déménageurs expérimentés, et un accent sur le service à la clientèle. Déménagement Vellour cherche à offrir une expérience de première classe à tous ses clients.</p>
  </section>

  <blockquote class="review one">
    <div class="stars">★★★★★</div>
    <p>Une super équipe qui travail avec soins et rapidité. J'ai eu une très belle expérience avec mon déménagement. Je recommande cette compagnie aux autres.</p>
  </blockquote>
  <blockquote class="review two">
    <div class="stars">★★★★★</div>
    <p>Equipe profesionnelle, employes très agréables et minutieux. Alex, Max et Léo : good job les gars merci beaucoup 10/10!!</p>
  </blockquote>

  <div class="fleet">
    <span role="img" aria-label="Photo d'une remorque fermée noire"></span>
    <span role="img" aria-label="Photo de camions de déménagement blancs"></span>
    <span role="img" aria-label="Photo d'une remorque noire ouverte"></span>
  </div>

  <div class="crew" role="img" aria-label="Photo de deux déménageurs souriants portant un tapis roulé et une boîte"></div>

  <footer class="contact">
    <div class="contact-phone">
      <svg width="12" height="15" viewBox="0 0 12 15"><rect x="1" y="1" width="10" height="13" rx="2" fill="none" stroke="currentColor" stroke-width="2"/><rect x="4" y="4" width="4" height="6" fill="currentColor"/></svg>
      438.555.0147
    </div>
    <div class="contact-web">www.demenagementvellour.com</div>
  </footer>
</main>
</body>
</html>
```